Verdant Medispa Business Card

need a business card for our medispa, attached please see the logo.
our website is https://verdantmedispa-example.com

Sorina Belcourt, MD
Internal Medicine

555-204-7193

Sorina@verdantmedispa-example.com

Www.Verdantmedispa-example.com

738 E Harlow Blvd N, Ste 512, Katy, TX 77981

Target Market(s)

MedSpa, Cosmetics, Esthetics

Industry/Entity Type

MedicalSpa

Contact Information for Business Card

Please see the attached business card which i pulled from the internet. I like the idea back as a logo and front with info.

Font styles to use
Decorative

Requirements
Must have
• Color should be matching with Logo and Website theme, Also I like to have QR code for the website

```html
<!DOCTYPE html>
<html lang="en">
<head>
<meta charset="utf-8">
<title>Verdant MediSpa Business Card</title>
<link href="https://fonts.googleapis.com/css2?family=Poppins:wght@400;600&display=swap" rel="stylesheet">
<style>
  :root {
    --backdrop: #d3d3d3;
    --card-white: #ffffff;
    --card-brown: #736150;
    --gold: #d4a52f;
    --gold-light: #f7e35a;
    --gold-deep: #c9972c;
    --ink: #1f1f1f;
    --muted: #555555;
    --dots: #6b6b6b;
    --qr-fill: #f4efe2;
  }
  * { box-sizing: border-box; margin: 0; padding: 0; }
  html, body { width: 1200px; height: 1200px; overflow: hidden; }
  body {
    background: var(--backdrop);
    font-family: "Poppins", sans-serif;
    position: relative;
  }
  .card {
    position: absolute;
    width: 720px;
    height: 410px;
    border-radius: 34px;
    overflow: hidden;
    box-shadow: 0 6px 14px rgba(0,0,0,0.18);
  }
  /* Front */
  .card-front {
    left: 70px; top: 130px;
    background: var(--card-white);
  }
  .front-edge {
    position: absolute; left: 0; right: 0; bottom: 0; height: 16px;
    background: linear-gradient(90deg, var(--gold-deep), var(--gold-light) 55%, var(--gold-deep));
  }
  .brand-front {
    position: absolute; right: 56px; top: 40px;
    color: var(--gold);
    font-weight: 600;
    font-size: 30px;
    line-height: 1;
  }
  .qr-code {
    position: absolute; right: 56px; top: 100px;
    width: 96px; height: 96px;
    background: var(--qr-fill);
    border: 2px solid var(--gold);
  }
  .person-name {
    position: absolute; left: 56px; top: 40px;
    color: var(--gold);
    font-weight: 600;
    font-size: 28px;
    line-height: 1.2;
  }
  .person-title {
    position: absolute; left: 56px; top: 80px;
    color: var(--muted);
    font-size: 16px;
  }
  .contact-list {
    position: absolute; left: 56px; top: 128px;
    list-style: none;
  }
  .contact-list li {
    display: flex; align-items: center; gap: 14px;
    font-size: 16px; color: var(--ink);
    margin-bottom: 10px;
    white-space: nowrap;
  }
  .contact-list svg { width: 22px; height: 22px; flex: none; }
  .appointment {
    position: absolute; left: 56px; right: 56px; bottom: 46px;
    display: flex; gap: 30px;
    font-size: 18px; color: var(--ink);
  }
  .appointment .field { flex: 1; display: flex; align-items: flex-end; gap: 8px; }
  .appointment .fill-line { flex: 1; border-bottom: 2px dotted var(--dots); margin-bottom: 7px; }
  /* Back */
  .card-back {
    left: 410px; top: 650px;
    background: var(--card-brown);
  }
  .brand-back {
    position: absolute; left: 0; right: 0; top: 150px;
    text-align: center;
    color: var(--gold);
    font-weight: 600;
    font-size: 64px;
    line-height: 1;
  }
  .back-bar {
    position: absolute; right: 70px; bottom: 34px; width: 330px; height: 22px;
    background: linear-gradient(90deg, var(--gold-deep), var(--gold-light) 55%, var(--gold-deep));
  }
</style>
</head>
<body>

<section class="card card-front" aria-label="Business card front">
  <div class="brand-front">Verdant MediSpa</div>
  <div class="qr-code" role="img" aria-label="QR code linking to the website"></div>

  <h1 class="person-name">Sorina Belcourt, MD</h1>
  <p class="person-title">Internal Medicine</p>

  <ul class="contact-list">
    <li>
      <svg viewBox="0 0 24 24" aria-hidden="true"><path fill="#d4a52f" d="M6.6 10.8a15 15 0 0 0 6.6 6.6l2.2-2.2a1 1 0 0 1 1-.25 11.4 11.4 0 0 0 3.6.57 1 1 0 0 1 1 1V20a1 1 0 0 1-1 1A17 17 0 0 1 3 4a1 1 0 0 1 1-1h3.5a1 1 0 0 1 1 1c0 1.25.2 2.45.57 3.6a1 1 0 0 1-.25 1z"/></svg>
      555-204-7193
    </li>
    <li>
      <svg viewBox="0 0 24 24" aria-hidden="true"><rect x="2" y="5" width="20" height="14" rx="1.5" fill="#d4a52f"/><path d="M3 6l9 7 9-7" fill="none" stroke="#fff" stroke-width="1.6"/></svg>
      Sorina@verdantmedispa-example.com
    </li>
    <li>
      <svg viewBox="0 0 24 24" aria-hidden="true"><g fill="none" stroke="#d4a52f" stroke-width="1.6"><circle cx="12" cy="12" r="9.5"/><ellipse cx="12" cy="12" rx="4" ry="9.5"/><path d="M2.5 12h19M4 7h16M4 17h16"/></g></svg>
      Www.Verdantmedispa-example.com
    </li>
    <li>
      <svg viewBox="0 0 24 24" aria-hidden="true"><path fill="#d4a52f" d="M12 2a7 7 0 0 0-7 7c0 5 7 13 7 13s7-8 7-13a7 7 0 0 0-7-7zm0 9.5A2.5 2.5 0 1 1 12 6.5a2.5 2.5 0 0 1 0 5z"/></svg>
      738 E Harlow Blvd N, Ste 512, Katy, TX 77981
    </li>
  </ul>

  <div class="appointment">
    <div class="field"><span>Date:</span><span class="fill-line"></span></div>
    <div class="field"><span>Time:</span><span class="fill-line"></span></div>
  </div>

  <div class="front-edge"></div>
</section>

<section class="card card-back" aria-label="Business card back">
  <div class="brand-back">Verdant MediSpa</div>
  <div class="back-bar"></div>
</section>

</body>
</html>
```